Quimby's Yard & Garden Center Business Card Update

I need an updated Business card design for my Lawn and Garden Center. We do Landscaping installs, Lawn Mowing, Snow Removal and also have a Garden Center Retail Division. I uploaded a few of our previous business cards to give an idea of what we are starting with. The main goal of this update is to simplify and modernize the business card, not all of the services that are on the previous cards has to be on the new one but I would still like to highlight our main services. There is also a sample of our logo that Can be used in the design.

Industry/Entity Type

Landscaping

Contact Information for Business Card

Morris Quimby
Morris@Quimbysyardandgarden.example
Business (555) 201-7784
Cell (555) 318-6092

Colors

Designer to choose colors to be used in the design.

Requirements
Must have
• Services Provided :
• Landscaping
• Lawn Maintenance
• Snow Removal
• Garden Center

```html
<!DOCTYPE html>
<html lang="en">
<head>
<meta charset="utf-8">
<title>Quimby's Yard &amp; Garden Center – Business Cards</title>
<link rel="stylesheet" href="https://fonts.googleapis.com/css2?family=Roboto+Condensed:wght@300;400;700&display=swap">
<style>
  :root {
    --backdrop: #2a2a2a;
    --card: #ffffff;
    --green: #2d5a27;
    --ink: #333333;
  }
  * { box-sizing: border-box; margin: 0; padding: 0; }
  html, body { width: 1200px; height: 852px; overflow: hidden; }
  body {
    background: var(--backdrop);
    font-family: "Roboto Condensed", sans-serif;
    display: flex; flex-direction: column; align-items: center; justify-content: center;
    gap: 40px;
  }
  .card {
    position: relative;
    width: 660px; height: 377px;
    background: var(--card);
    box-shadow: 0 10px 30px rgba(0,0,0,.45);
  }
  .brand {
    position: absolute; right: 70px; top: 70px;
    display: flex; align-items: center; gap: 14px;
  }
  .brand-dot { width: 30px; height: 30px; border-radius: 50%; background: var(--green); }
  .brand-name { font-size: 56px; font-weight: 700; color: var(--green); line-height: 1; }
  .services { position: absolute; left: 48px; bottom: 48px; }
  .services-title { color: var(--green); font-weight: 700; font-size: 22px; letter-spacing: .5px; margin-bottom: 8px; }
  .services-line { color: var(--ink); font-size: 20px; font-weight: 300; line-height: 1.35; }
  .contact { position: absolute; left: 48px; bottom: 40px; }
  .person-name { color: var(--green); font-size: 28px; font-weight: 400; letter-spacing: 1px; }
  .person-role { color: var(--ink); font-size: 17px; font-weight: 300; margin: 2px 0 14px; }
  .contact-row { display: flex; align-items: center; gap: 10px; color: var(--ink); font-size: 17px; font-weight: 300; line-height: 1.55; }
  .contact-row svg { width: 13px; height: 13px; flex: none; }
</style>
</head>
<body>
  <section class="card card-front">
    <div class="brand">
      <span class="brand-dot"></span>
      <span class="brand-name">Quimby's</span>
    </div>
    <div class="services">
      <p class="services-title">SERVICES PROVIDED :</p>
      <p class="services-line">Landscaping | Lawn Maintenance</p>
      <p class="services-line">Snow Removal | Garden Center</p>
    </div>
  </section>

  <section class="card card-back">
    <div class="brand">
      <span class="brand-dot"></span>
      <span class="brand-name">Quimby's</span>
    </div>
    <div class="contact">
      <p class="person-name">MORRIS QUIMBY</p>
      <p class="person-role">Director</p>
      <p class="contact-row">
        <svg viewBox="0 0 16 16" aria-hidden="true"><path d="M4 1l3 3-2 2c1 2 3 4 5 5l2-2 3 3-2 2C7 14 2 9 2 3z" fill="var(--green)"/></svg>
        (555) 201-7784
      </p>
      <p class="contact-row">
        <svg viewBox="0 0 16 16" aria-hidden="true"><rect x="4" y="1" width="8" height="14" rx="1.5" fill="none" stroke="var(--green)" stroke-width="2"/></svg>
        (555) 318-6092
      </p>
      <p class="contact-row">
        <svg viewBox="0 0 16 16" aria-hidden="true"><rect x="1" y="3" width="14" height="10" fill="none" stroke="var(--green)" stroke-width="1.6"/><path d="M1 3l7 6 7-6" fill="none" stroke="var(--green)" stroke-width="1.6"/></svg>
        Morris@Quimbysyardandgarden.example
      </p>
      <p class="contact-row">
        <svg viewBox="0 0 16 16" aria-hidden="true"><circle cx="8" cy="8" r="6.5" fill="none" stroke="var(--green)" stroke-width="1.5"/><ellipse cx="8" cy="8" rx="3" ry="6.5" fill="none" stroke="var(--green)" stroke-width="1.2"/><path d="M1.5 8h13" stroke="var(--green)" stroke-width="1.2"/></svg>
        www.Quimbysyardandgarden.example
      </p>
    </div>
  </section>
</body>
</html>
```